Bref créative |
Tern Ledger | ||
Business Cards and Letterheads | ||
Use standard fonts | ||
Cutting-Edge Professional Simple |
Ronald Pyke | ||
Suite 412, Level 4, 35 Gorse St, Sydney, NSW, 2000 | ||
ronald@ternledger-example.com | ||
www.ternledger-example.com | ||
Good Luck! | ||
<< Up to the designer >> | ||

```html
<!DOCTYPE html>
<html lang="en">
<head>
<meta charset="utf-8">
<title>Tern Ledger — Letterheads</title>
<link href="https://fonts.googleapis.com/css2?family=Montserrat:wght@400;700&display=swap" rel="stylesheet">
<style>
  :root {
    --backdrop: #2a2a2a;
    --paper: #ffffff;
    --ink: #3a3a3a;
    --ink-soft: #8a8a8a;
    --rule: #c9c9c9;
    --accent: #f0a81c;
  }
  * { margin: 0; padding: 0; box-sizing: border-box; }
  html, body { width: 1200px; height: 737px; overflow: hidden; background: var(--backdrop); }
  body { font-family: "Montserrat", Arial, sans-serif; position: relative; }

  .letterhead {
    position: absolute;
    top: 29px;
    width: 480px;
    height: 672px;
    background: var(--paper);
    overflow: hidden;
  }
  .letterhead--front { left: 77px; }
  .letterhead--continuation { left: 653px; }

  .corner-ring { position: absolute; top: 0; right: 0; }

  .brand {
    position: absolute;
    left: 36px;
    top: 52px;
    display: flex;
    align-items: center;
    gap: 6px;
  }
  .brand__dot {
    width: 9px; height: 9px;
    border-radius: 50%;
    background: var(--accent);
  }
  .brand__name {
    font-size: 10px;
    font-weight: 700;
    letter-spacing: 0.3px;
    text-transform: uppercase;
    color: var(--ink);
  }

  .header-rule {
    position: absolute;
    left: 36px; right: 30px;
    top: 77px;
    height: 1px;
    background: var(--rule);
  }

  .contact-lines {
    position: absolute;
    right: 30px;
    top: 84px;
    text-align: right;
    font-size: 6.5px;
    line-height: 10px;
    color: var(--ink-soft);
  }

  .footer-address {
    position: absolute;
    left: 27px;
    top: 620px;
    font-size: 6.5px;
    line-height: 10px;
    color: var(--ink-soft);
    max-width: 150px;
  }
  .footer-email {
    position: absolute;
    right: 30px;
    top: 632px;
    font-size: 6.5px;
    color: var(--ink-soft);
  }
  .footer-rule {
    position: absolute;
    left: 27px; right: 30px;
    top: 645px;
    height: 1px;
    background: var(--rule);
  }
</style>
</head>
<body>

  <section class="letterhead letterhead--front">
    <svg class="corner-ring" width="90" height="80" viewBox="0 0 90 80">
      <circle cx="60" cy="14" r="38" fill="none" stroke="var(--accent)" stroke-width="14"/>
    </svg>
    <div class="brand"><span class="brand__dot"></span><span class="brand__name">Tern Ledger</span></div>
    <div class="header-rule"></div>
    <div class="contact-lines">
      <p>Phone +61 2 5550 0142</p>
      <p>Cell +61 400 555 018</p>
      <p>Fax +61 2 5550 0143</p>
    </div>
    <p class="footer-address">Suite 412, Level 4, 35 Gorse St,<br>Sydney, NSW, 2000</p>
    <p class="footer-email">Email : ronald@ternledger-example.com</p>
    <div class="footer-rule"></div>
  </section>

  <section class="letterhead letterhead--continuation">
    <svg class="corner-ring" width="90" height="100" viewBox="0 0 90 100">
      <circle cx="62" cy="40" r="24" fill="none" stroke="var(--accent)" stroke-width="12"/>
    </svg>
    <div class="brand"><span class="brand__dot"></span><span class="brand__name">Tern Ledger</span></div>
    <div class="header-rule"></div>
    <div class="contact-lines">
      <p>Phone +61 2 5550 0142</p>
      <p>Cell +61 400 555 018</p>
      <p>Fax +61 2 5550 0143</p>
    </div>
    <p class="footer-address">Suite 412, Level 4, 35 Gorse St,<br>Sydney, NSW, 2000</p>
    <p class="footer-email">Email : ronald@ternledger-example.com</p>
    <div class="footer-rule"></div>
  </section>

</body>
</html>
```